BRISKET Homes business card Pelmo Press

I've been a Real Estate agent since 1988. I left the BIG brokerages 2 years ago and am on my own and need a business card. I love doing graphics, but don't have the bandwidth right now.

Background. I want a card that stands out like I do. I'm the fun guy that always has a joke or funny story, and my clients like me. Something fun, but not too silly.

I don't have a symbol or logo that I'm using on the card now, but need to include something, a Font by itself or a logo? I'm not sure if we need a logo or not. I'm open.
The GREAT design is going to be the basis for the next project of stationary, note pads, and Real Estate FOR SALE & Open House signs.

Single sided card is fine, but I selected a 2 sided just in case that's what it works out to be.

Here we go. If you need anything else. Please let me know. As I think of anything, I'll add that also.

Target Market(s)

My territory is Santa Clara County / Silicon Valley, CA. I tend to work with new buyers buying a condo ($500,000) up to single family home for about $1.5 million. 1st time buyers and also move-up buyers. I haven't worked with multi-million $$ homes .... but wouldn't turn it down. Clients here tend to be White, Latin and now many more Chinese and East Indians. Clients also tend to be high tech, Zorvat, Quince, Lumigrid workers and also non tech people.

Industry/Entity Type

Business

Contact Information for Business Card

CONTENT:
Company: BRISKET Homes
My name: Harold P. Brisket Jr.
Title: Real Estate Broker
Email: Hal@HaroldBrisket.example
Website: www.HaroldBrisket.example
Phone: (408) 555-0173
BRE # 07395162

Font styles to use
Sans Serif

Requirements
Must have
• Content from above. Something that stands out from the others. Serious enough looking, not stale, maybe a bit fun.

```html
<!DOCTYPE html>
<html lang="en">
<head>
<meta charset="utf-8">
<title>BRISKET Homes — Business Card</title>
<link href="https://fonts.googleapis.com/css2?family=Josefin+Sans:wght@300&family=Tinos:wght@400&display=swap" rel="stylesheet">
<style>
  :root {
    --canvas: #3b3c40;
    --card-black: #1d1d1f;
    --card-white: #ffffff;
    --gold: #cfae45;
    --ink: #1a1a1a;
    --ink-soft: #333333;
  }
  * { margin: 0; padding: 0; box-sizing: border-box; }
  html, body {
    width: 1200px;
    height: 1000px;
    overflow: hidden;
    background: var(--canvas);
  }
  .canvas {
    position: relative;
    width: 1200px;
    height: 1000px;
  }
  .card {
    position: absolute;
    left: 250px;
    width: 700px;
    height: 400px;
    overflow: hidden;
    box-shadow: 0 10px 30px rgba(0,0,0,0.35);
  }
  .card--front { top: 70px; background: var(--card-white); }
  .card--back  { top: 530px; background: var(--card-black); }

  .wordmark {
    font-family: "Josefin Sans", sans-serif;
    font-weight: 300;
    color: var(--gold);
    line-height: 1;
    text-align: right;
  }
  .wordmark__name { display: block; letter-spacing: 0.02em; }
  .wordmark__sub  { display: block; letter-spacing: 0.32em; margin-right: -0.32em; }

  /* Front */
  .front__band {
    position: absolute;
    top: 0; left: 0; right: 0;
    height: 118px;
    background: var(--card-black);
  }
  .front__band .wordmark {
    position: absolute;
    right: 34px;
    top: 28px;
  }
  .front__band .wordmark__name { font-size: 48px; }
  .front__band .wordmark__sub  { font-size: 17px; margin-top: 2px; }

  .front__identity {
    position: absolute;
    top: 190px;
    left: 0; right: 0;
    text-align: center;
    font-family: "Tinos", serif;
    color: var(--ink);
  }
  .identity__name  { font-size: 24px; letter-spacing: 0.02em; }
  .identity__title { font-size: 16px; margin-top: 2px; }

  .front__contact {
    position: absolute;
    left: 34px;
    bottom: 28px;
    list-style: none;
    font-family: "Tinos", serif;
    font-size: 14px;
    line-height: 1.4;
    color: var(--ink-soft);
  }

  /* Back */
  .card--back .wordmark {
    position: absolute;
    left: 0; right: 0;
    top: 120px;
    text-align: center;
  }
  .card--back .wordmark__name { font-size: 112px; }
  .card--back .wordmark__sub  { font-size: 38px; margin-top: 8px; text-align: right; padding-right: 70px; }
</style>
</head>
<body>
<main class="canvas">

  <section class="card card--front" aria-label="Card front">
    <header class="front__band">
      <div class="wordmark">
        <span class="wordmark__name">BRISKET</span>
        <span class="wordmark__sub">HOMES</span>
      </div>
    </header>
    <div class="front__identity">
      <p class="identity__name">HAROLD P. BRISKET JR.</p>
      <p class="identity__title">Real Estate Broker</p>
    </div>
    <ul class="front__contact">
      <li>Hal@HaroldBrisket.example</li>
      <li>www.HaroldBrisket.example</li>
      <li>Phone: (408) 555-0173</li>
      <li>BRE # 07395162</li>
    </ul>
  </section>

  <section class="card card--back" aria-label="Card back">
    <div class="wordmark">
      <span class="wordmark__name">BRISKET</span>
      <span class="wordmark__sub">HOMES</span>
    </div>
  </section>

</main>
</body>
</html>
```